Flyer Design Project

We need a flyer design for a 1 year old domestic cleaning company based in Wiltshire, England. We provide households with high quality, hard working cleaners. We would like to see designs which use blue (the colour on the logo attatched). The final design should communicate a clean, premier and thorough service in a clear and bold way. We would like the flyer to be A5 with a single sided design. We have attached an A5 word document with the words we would like to be used in the design, what we need is for you to give it some life, colour, artwork and a professional touch. We are perfectionsists which we would like to illustrate to our customer through this flyer.
Updates

payment has been guaranteed!

Sorry..... please no pictures of females on the designs. many thanks

Target Market(s)

females with higher than average income, aged 30-50. Have families and work 9-5.

Industry/Entity Type

It Company

Requirements
Must have
• The flyer must include the logo attatched and the words in the A5 document attatched. With RELIABLE CLEANERS preferably the headline. A5 - single sided.
The Flyer must also include our introductory offer.....
First Clean FREE
Allow us to demonstrate our standards

this should be emphasised.

PLEASE NOTE: can this be added to the list of words on the flyer please:

Ironing service - one day turn around
Nice to have
• some pictures - nothing cheesey. Again, pictures should communicate our modern professional approach.

```html
<!DOCTYPE html>
<html lang="en">
<head>
<meta charset="utf-8">
<title>Larkmoor Cleaners – Flyer</title>
<link rel="stylesheet" href="https://fonts.googleapis.com/css2?family=Caladea:wght@400;700&family=PT+Sans:wght@400&display=swap">
<style>
  :root {
    --page-bg: #e9e6e1;
    --brand-blue: #1a6bc0;
    --brand-blue-deep: #0b4f94;
    --panel-grey: #dcdcdd;
    --ring-grey: #e7e7e8;
    --ink: #141414;
    --white: #ffffff;
    --bullet-gold: #d4b52a;
    --photo-dark: #4a2a16;
    --photo-mid: #9a5a2c;
    --photo-light: #c98a52;
  }
  * { margin: 0; padding: 0; box-sizing: border-box; }
  html, body {
    width: 1200px; height: 924px; overflow: hidden;
    background: var(--page-bg);
  }
  .canvas { position: relative; width: 1200px; height: 924px; }
  .flyer {
    position: absolute; left: 20px; top: 58px;
    width: 890px; height: 620px;
    transform: scale(1.3034); transform-origin: 0 0;
    overflow: hidden; background: var(--panel-grey);
    font-family: "Caladea", Georgia, serif;
  }
  .flyer-art { position: absolute; inset: 0; width: 890px; height: 620px; }

  .headline, .offer, .intro, .benefits li, .ironing-badge__text {
    color: var(--white);
    text-shadow: 1px 1px 2px rgba(0,0,0,.75);
  }
  .headline {
    position: absolute; left: 20px; top: 8px;
    font-size: 40px; font-weight: 400; letter-spacing: 1px;
  }
  .offer {
    position: absolute; left: 220px; top: 56px;
    font-size: 45px; font-weight: 400; letter-spacing: 1px;
  }
  .intro {
    position: absolute; left: 205px; top: 114px;
    font-size: 15.5px; letter-spacing: .3px;
  }
  .benefits { position: absolute; top: 139px; list-style: none; }
  .benefits--left { left: 203px; }
  .benefits--right { left: 428px; }
  .benefits li {
    position: relative; padding-left: 20px;
    font-size: 16px; line-height: 22.5px; letter-spacing: .3px;
  }
  .benefits li::before {
    content: ""; position: absolute; left: 0; top: 7px;
    width: 11px; height: 9px; border-radius: 50%;
    background: radial-gradient(circle at 35% 35%, #f3e07a, var(--bullet-gold) 60%, #8a7110);
  }

  .ironing-badge__text {
    position: absolute; left: 700px; top: 76px; width: 180px;
    text-align: center; font-size: 16.5px; line-height: 22px; letter-spacing: .4px;
  }
  .ironing-badge__text strong { font-weight: 700; }

  .brand {
    position: absolute; left: 30px; top: 426px;
    display: flex; align-items: center; gap: 14px;
  }
  .brand__mark { width: 54px; height: 54px; background: var(--brand-blue); }
  .brand__name {
    font-family: "PT Sans", Arial, sans-serif;
    font-size: 41px; line-height: 54px; color: var(--ink); letter-spacing: .2px;
    white-space: nowrap;
  }
  .tagline {
    position: absolute; left: 120px; top: 502px;
    font-family: "PT Sans", Arial, sans-serif;
    font-size: 22px; color: var(--ink);
  }

  .contact {
    position: absolute; top: 568px; height: 34px;
    border-radius: 4px; padding: 0 8px;
    display: flex; align-items: center;
    background: linear-gradient(var(--brand-blue), var(--brand-blue-deep));
    box-shadow: 1px 2px 3px rgba(0,0,0,.4);
    color: var(--white); font-size: 18.5px; letter-spacing: .4px; white-space: nowrap;
  }
  .contact--email { left: 14px; width: 388px; }
  .contact--phone { left: 407px; width: 298px; }
</style>
</head>
<body>
<main class="canvas">
  <section class="flyer">
    <svg class="flyer-art" viewBox="0 0 890 620" xmlns="http://www.w3.org/2000/svg">
      <defs>
        <linearGradient id="floorTone" x1="0" y1="0" x2="1" y2="1">
          <stop offset="0" stop-color="var(--photo-mid)"/>
          <stop offset=".45" stop-color="var(--photo-light)"/>
          <stop offset="1" stop-color="var(--photo-dark)"/>
        </linearGradient>
        <linearGradient id="dusterTone" x1="0" y1="0" x2="1" y2="1">
          <stop offset="0" stop-color="#c43a2a"/>
          <stop offset="1" stop-color="#6b2a1a"/>
        </linearGradient>
        <linearGradient id="roomTone" x1="0" y1="0" x2="0" y2="1">
          <stop offset="0" stop-color="#d9d6cf"/>
          <stop offset="1" stop-color="#7d5a3e"/>
        </linearGradient>
        <linearGradient id="sinkTone" x1="0" y1="0" x2="1" y2="1">
          <stop offset="0" stop-color="#b08a62"/>
          <stop offset="1" stop-color="#e9e6e2"/>
        </linearGradient>
        <radialGradient id="badgeTone" cx=".4" cy=".35" r=".75">
          <stop offset="0" stop-color="#2f86d6"/>
          <stop offset="1" stop-color="#0a3f7a"/>
        </radialGradient>
      </defs>

      <rect class="hero-photo" x="0" y="0" width="890" height="620" fill="url(#floorTone)"
            role="img" aria-label="Photo of a floor polishing machine on a polished wooden floor, a cleaner's legs behind it"/>

      <polygon class="accent-band" points="0,130 890,545 890,566 0,200" fill="var(--brand-blue)"/>
      <polygon class="info-panel" points="0,200 890,566 890,620 0,620" fill="var(--panel-grey)"/>

      <polygon class="ironing-badge" fill="url(#badgeTone)" stroke="#0a3f7a" stroke-width="1"
        points="790,14 802,36 820,20 826,44 846,34 846,58 868,54 862,76 882,80 870,98 888,108 870,120 884,136 862,140 870,160 848,158 848,182 826,172 820,196 802,180 790,200 778,180 760,196 754,172 732,182 732,158 710,160 718,140 696,136 710,120 692,108 710,98 698,80 718,76 712,54 734,58 734,34 754,44 760,20 778,36"/>

      <circle cx="365" cy="305" r="104" fill="var(--ring-grey)"/>
      <circle cx="365" cy="305" r="91" fill="url(#dusterTone)"
              role="img" aria-label="Photo of a feather duster cleaning a wooden surface"/>
      <circle cx="615" cy="420" r="84" fill="var(--ring-grey)"/>
      <circle cx="615" cy="420" r="72" fill="url(#roomTone)"
              role="img" aria-label="Photo of a man vacuuming a bright living room"/>
      <circle cx="790" cy="517" r="58" fill="var(--ring-grey)"/>
      <circle cx="790" cy="517" r="48" fill="url(#sinkTone)"
              role="img" aria-label="Photo of a hand washing a plate with a green sponge"/>
    </svg>

    <h1 class="headline">Reliable Cleaners!</h1>
    <h2 class="offer">First Clean FREE</h2>
    <p class="intro">Allow us to demonstrate our standards......</p>
    <ul class="benefits benefits--left">
      <li>Personalised Service</li>
      <li>Constantly Thorough</li>
      <li>Hassel Free</li>
    </ul>
    <ul class="benefits benefits--right">
      <li>Insured</li>
      <li>Regular Weekly Claims</li>
      <li>No Contracts</li>
    </ul>

    <p class="ironing-badge__text"><strong>Ironing Service</strong><br>One Day<br>Turn Around</p>

    <div class="brand">
      <span class="brand__mark"></span>
      <span class="brand__name">Larkmoor Cleaners</span>
    </div>
    <p class="tagline">Premier Domestic Cleaners</p>

    <p class="contact contact--email">Email: larkmoorcleaners@example.co.uk</p>
    <p class="contact contact--phone">Call our hotline: 07700900123</p>
  </section>
</main>
</body>
</html>
```